Designing a brochures for an educational counseling service provider

We would like a 4 sided design on a 11x8.5 paper, half folded. I have including a sample design we did to give you an idea of what we envision but we welcome creativity to make beautiful looking flyers. Text for the flier is included as well as our logo.
- The most important thing is capturing our audience/market. We will be handing these flies to schools, organizations and individual clients.

www.plorvaeducationalconsultants.example

Target Market(s)

We are targeting international students wanting to study in the U.S and Canada.

Industry/Entity Type

Education

Requirements
Must have
• - Clean and clear
• - Our logo should visible and well placed.
• - Could you the pictures of students, libraries and school buildings or you could use the pictures we already have.
Nice to have
• We would like this to match business cards.

```html
<!DOCTYPE html>
<html lang="en">
<head>
<meta charset="utf-8">
<title>Plorva Brochure Spread</title>
<link rel="stylesheet" href="https://fonts.googleapis.com/css2?family=Raleway:wght@400;500;600;700;800&family=Open+Sans:wght@600;700&display=swap">
<style>
  :root {
    --navy: #1f2f8a;
    --blue: #2c5fb8;
    --blue-light: #3a86d1;
    --green: #6cc644;
    --green-dark: #4fae2f;
    --ink: #2b2b2b;
    --paper: #ffffff;
    --bg: #e9e6e1;
  }
  * { margin: 0; padding: 0; box-sizing: border-box; }
  html, body { width: 1200px; height: 900px; overflow: hidden; }
  body {
    background: var(--bg);
    font-family: "Raleway", Arial, sans-serif;
    color: var(--ink);
    position: relative;
  }
  .spread {
    position: absolute;
    left: 70px; top: 40px;
    width: 1060px; height: 820px;
    display: flex;
    box-shadow: 0 10px 30px rgba(0,0,0,.18);
  }
  .page {
    position: relative;
    width: 530px; height: 820px;
    background: var(--paper);
    overflow: hidden;
  }
  .page--back { border-right: 1px solid #ddd; }

  /* back page */
  .services { padding: 34px 34px 0 34px; height: 330px; }
  .service-label {
    display: inline-block;
    background: var(--green);
    color: #fff;
    font-family: "Open Sans", Arial, sans-serif;
    font-weight: 700;
    font-size: 13px;
    padding: 3px 40px 3px 10px;
    margin-bottom: 6px;
  }
  .service-text {
    font-size: 13px;
    line-height: 1.32;
    color: var(--ink);
    margin-bottom: 8px;
  }
  .photo { position: absolute; }
  .photo--team {
    left: 0; top: 330px; width: 530px; height: 235px;
    background: linear-gradient(180deg, #d9e3c7 0%, #b8c9a0 35%, #e8e6e4 70%, #f3f3f3 100%);
  }
  .contact-block {
    position: absolute; left: 0; top: 565px; width: 530px; height: 217px;
    display: flex; align-items: center;
    padding: 0 20px 0 26px;
  }
  .brand { display: flex; align-items: center; gap: 8px; }
  .brand-dot {
    width: 24px; height: 24px; border-radius: 50%;
    background: var(--green);
    flex: none;
  }
  .brand-name {
    font-family: "Raleway", Arial, sans-serif;
    font-weight: 800;
    color: var(--navy);
    font-size: 28px;
    letter-spacing: 1px;
    line-height: 1;
  }
  .brand-sub {
    font-weight: 700;
    color: var(--navy);
    font-size: 8px;
    line-height: 1.3;
    text-transform: uppercase;
    margin-top: 5px;
    white-space: nowrap;
  }
  .brand-wrap { width: 180px; flex: none; }
  .divider {
    width: 1px; height: 120px; background: var(--green);
    margin: 0 12px 0 8px;
    flex: none;
  }
  .contact { font-size: 10.5px; line-height: 1.4; color: var(--ink); white-space: nowrap; }
  .contact-title {
    color: var(--green-dark);
    font-family: "Open Sans", Arial, sans-serif;
    font-weight: 700; font-size: 11px; text-transform: uppercase;
  }
  .contact-role { font-weight: 700; font-size: 11.5px; line-height: 1.3; margin-bottom: 2px; }
  .back-strip {
    position: absolute; left: 0; bottom: 0; width: 530px; height: 38px;
    background: linear-gradient(90deg, var(--navy), var(--blue));
  }

  /* front page */
  .photo--students {
    left: 0; top: 170px; width: 530px; height: 420px;
    background: linear-gradient(160deg, #6f9a4e 0%, #9bbf7a 35%, #c9b39e 65%, #7fa0c7 100%);
  }
  .front-curve { position: absolute; left: 0; top: 0; }
  .front-brand { position: absolute; right: 55px; top: 60px; }
  .tagline {
    position: absolute; left: 0; top: 585px; width: 530px; height: 66px;
    background: var(--green);
    color: #fff;
    font-family: "Open Sans", Arial, sans-serif;
    font-weight: 700; font-size: 16px; line-height: 1.25;
    text-align: center;
    display: flex; align-items: center; justify-content: center;
    padding: 0 20px;
  }
  .offer-band {
    position: absolute; left: 0; top: 651px; width: 530px; height: 130px;
    background: linear-gradient(90deg, var(--navy) 0%, var(--blue) 55%, var(--blue-light) 100%);
    display: flex; justify-content: space-around; align-items: center;
    padding: 0 14px;
  }
  .offer { text-align: center; color: #fff; width: 110px; }
  .offer svg { display: block; margin: 0 auto 8px; }
  .offer-name { font-size: 11px; font-weight: 600; }
  .front-strip {
    position: absolute; left: 0; bottom: 0; width: 530px; height: 30px;
    background: var(--navy);
    border-top: 6px solid #fff;
  }
</style>
</head>
<body>
<main class="spread">

  <section class="page page--back">
    <div class="services">
      <span class="service-label">Transfer students</span>
      <p class="service-text">Need to find a school an alternative school that is a better match for you? We work with students and families to transfer from one school to another.</p>
      <span class="service-label">Boarding schools</span>
      <p class="service-text">Funding the education for your children in some of the world's top schools can be very expensive as tuition and fees increase at an average of 4% every year. We work with you to determine the budget for your family, applying to scholarship available and guide you through the financial aid process.</p>
      <p class="service-text">Over 70% of our clients have been awarded scholarships or Financial Aid, making your education goals attainable an affordable and your children education possible.</p>
      <p class="service-text">Include at the bottom of last page "Our consultants are members of Halvern Guild, the leading association for educational consultants in North America"</p>
    </div>

    <div class="photo photo--team" role="img" aria-label="Photo of a smiling girls' soccer team in white jerseys on a field"></div>

    <div class="contact-block">
      <div class="brand-wrap">
        <div class="brand">
          <span class="brand-dot"></span>
          <span class="brand-name">PLORVA</span>
        </div>
        <div class="brand-sub">International Educational Consultants<br>International Students Solutions</div>
      </div>
      <div class="divider"></div>
      <div class="contact">
        <div class="contact-title">Contact us</div>
        <div class="contact-role">Executive Director &amp; Independent<br>Educational Consultant</div>
        <div>Plorva International Educational Consultants, LLC,</div>
        <div>1180 Meadow Rd, Suite 210, Lakeside, TX 75010</div>
        <div>Phone: 555-014-2290,</div>
        <div>Email: info@plorvaeducationalconsultants.example</div>
        <div>www.plorvaeducationalconsultants.example</div>
      </div>
    </div>

    <div class="back-strip"></div>
  </section>

  <section class="page page--front">
    <div class="photo photo--students" role="img" aria-label="Photo of a group of smiling college students holding notebooks outdoors"></div>

    <svg class="front-curve" width="530" height="600" viewBox="0 0 530 600" aria-hidden="true">
      <path d="M0 0 H530 V560 C500 380 400 230 0 180 Z" fill="#ffffff"/>
      <path d="M250 200 C420 250 500 380 530 540" fill="none" stroke="#1f2f8a" stroke-width="7"/>
    </svg>

    <div class="front-brand brand-wrap">
      <div class="brand">
        <span class="brand-dot"></span>
        <span class="brand-name">PLORVA</span>
      </div>
      <div class="brand-sub">International Educational Consultants<br>International Students Solutions</div>
    </div>

    <div class="tagline">A full - service international educational consulting group serving students and families across the globe</div>

    <div class="offer-band">
      <div class="offer">
        <svg width="50" height="50" viewBox="0 0 50 50" aria-hidden="true" fill="none" stroke="#fff" stroke-width="1.6">
          <circle cx="25" cy="25" r="23"/>
          <path d="M14 21 L25 14 L36 21 Z M15 23 H35 M17 24 V33 M22 24 V33 M28 24 V33 M33 24 V33 M14 35 H36"/>
        </svg>
        <div class="offer-name">Boarding Schools</div>
      </div>
      <div class="offer">
        <svg width="50" height="50" viewBox="0 0 50 50" aria-hidden="true" fill="none" stroke="#fff" stroke-width="1.6">
          <circle cx="25" cy="25" r="23"/>
          <path d="M16 14 H30 L34 18 V36 H16 Z M20 22 H30 M20 26 H30 M20 30 H26 M27 34 L36 25"/>
        </svg>
        <div class="offer-name">College Admission</div>
      </div>
      <div class="offer">
        <svg width="50" height="50" viewBox="0 0 50 50" aria-hidden="true" fill="none" stroke="#fff" stroke-width="1.6">
          <circle cx="25" cy="25" r="23"/>
          <circle cx="19" cy="19" r="4"/>
          <circle cx="31" cy="19" r="4"/>
          <path d="M12 32 C12 26 26 26 26 32 M24 32 C24 26 38 26 38 32 M12 34 H38"/>
        </svg>
        <div class="offer-name">Transfer Students</div>
      </div>
      <div class="offer">
        <svg width="50" height="50" viewBox="0 0 50 50" aria-hidden="true" fill="none" stroke="#fff" stroke-width="1.6">
          <circle cx="25" cy="25" r="23"/>
          <path d="M11 21 L25 15 L39 21 L25 27 Z M17 24 V31 C21 35 29 35 33 31 V24 M37 22 V30"/>
        </svg>
        <div class="offer-name">Graduate Students</div>
      </div>
    </div>

    <div class="front-strip"></div>
  </section>

</main>
</body>
</html>
```